Update patient consent forms and contract

Objective
Redesign the existing patient contract information document to create a modern,contempory, and easy-to-understand experience for patients. The updated design should improve readability, accessibility, and overall presentation while maintaining compliance with healthcare and legal requirements.

Key Deliverables

Refreshed visual design and layout
Improved information hierarchy and readability
Modern typography and colour palette aligned with brand guidelines
Clear section headings and navigation
Print-ready and digital versions (PDF)

Include KEV Logo within patient KEV consent to treatment. Ideally this document should be portrait not landscape.
Updates

I would love a front page to be included in the document

```html
<!DOCTYPE html>
<html lang="en">
<head>
<meta charset="utf-8">
<title>Halden Orthodontics – Patient Information &amp; Consent Pack</title>
<link href="https://fonts.googleapis.com/css2?family=Inter:wght@400;500;600;700&display=swap" rel="stylesheet">
<style>
:root{
  --backdrop:#dcdcdc;
  --navy:#1d3553;
  --accent:#1aa3d4;
  --brand-grey:#8b9097;
  --text:#4a4f55;
  --rule:#e3e7eb;
  --pale:#eaf5fa;
  --pale-2:#f3f9fc;
  --cover-bg:#eef7fb;
  --circle-1:#dff0f7;
  --circle-2:#bfe5f3;
  --note-bg:#fff7ea;
  --note-line:#f0c27a;
}
*{box-sizing:border-box;margin:0;padding:0}
html,body{width:1200px;height:927px;overflow:hidden;background:var(--backdrop);font-family:"Inter",Arial,sans-serif}
.stage{position:absolute;left:0;top:0;width:2184px;height:1688px;transform:scale(0.5495);transform-origin:0 0}
.page{position:absolute;width:456px;height:645px;background:#fff;box-shadow:0 3px 9px rgba(0,0,0,.35);overflow:hidden}
.inner{padding:36px 48px 0 48px}
.brand{font-size:13px;font-weight:600;color:var(--brand-grey);padding-bottom:5px;border-bottom:1px solid var(--rule);letter-spacing:.2px}
.brand .dot{display:inline-block;width:6px;height:6px;border-radius:50%;background:var(--accent);margin-right:4px;vertical-align:2px}
.sec-head{border-left:6px solid var(--accent);padding-left:8px;margin:18px 0 12px 5px}
.sec-head h2{font-size:9.5px;font-weight:600;color:var(--navy);line-height:1.25}
.sec-head .sub{font-size:8.4px;color:#555;line-height:1.25}
h3{font-size:8.6px;font-weight:500;color:var(--navy);margin:9px 0 4px}
h4{font-size:6.8px;font-weight:600;color:var(--navy);margin:8px 0 1px}
p{font-size:5.5px;line-height:1.55;color:var(--text);margin-bottom:4px}
.box{border:1px solid #8fd0e8;background:var(--pale-2);padding:7px 7px;margin:8px 0}
.box.note{border-color:var(--note-line);background:var(--note-bg)}
.box-title{font-size:6px;font-weight:600;color:var(--navy);margin-bottom:8px}
footer{position:absolute;left:48px;right:48px;bottom:26px;border-top:1px solid var(--rule);padding-top:5px;display:flex;justify-content:space-between;font-size:4.4px}
footer .org{color:var(--accent);font-weight:600}
footer .num{color:var(--brand-grey)}
.kev{display:flex;align-items:center;gap:5px;color:var(--navy);font-size:11px;font-weight:500}
.kev .mark{width:16px;height:16px;border-radius:50%;background:#b8bec4}
.field{font-size:5.5px;font-weight:600;color:var(--navy);margin:9px 0}
.field .line{display:inline-block;border-bottom:.6px solid #999;height:5px;vertical-align:-1px}
.option{display:flex;gap:12px;border:1px solid var(--rule);background:#fafcfd;padding:7px 8px;margin-bottom:7px}
.option .check{font-size:7px;font-weight:600;color:var(--navy)}
.option strong{font-size:5.5px;color:var(--navy);display:block}

/* cover */
.cover{background:var(--cover-bg)}
.cover .panel{position:absolute;left:34px;top:36px;width:390px;height:574px;background:#fff;border-radius:14px}
.cover .deco{position:absolute;left:0;top:0}
.cover .band{position:absolute;left:0;bottom:0;width:100%;height:15px;background:var(--accent)}
.cover .logo{position:absolute;left:152px;top:98px;font-size:19px;font-weight:600;color:var(--brand-grey)}
.cover h1{position:absolute;left:53px;top:215px;font-size:21.5px;line-height:1.22;font-weight:700;color:var(--navy)}
.cover .tag{position:absolute;left:53px;top:280px;font-size:9px;color:#6c7379}
.prep{position:absolute;left:66px;top:310px;width:326px;height:35px;border:1px solid var(--rule);padding:6px 7px;display:flex;justify-content:space-between;font-size:5.5px;font-weight:600;color:var(--navy)}
.steps{position:absolute;left:66px;top:368px;width:326px;height:35px;display:flex;background:var(--pale)}
.steps div{flex:1;padding:6px 6px;font-size:5.5px;color:var(--navy);border-right:1px solid #fff;line-height:1.8}
.partner{position:absolute;left:68px;top:425px;width:322px;height:74px;border:1px solid var(--rule);display:flex;align-items:center;gap:14px;padding:0 10px}
.partner p{font-size:5.3px;margin:0}
</style>
</head>
<body>
<div class="stage">

  <!-- Cover -->
  <section class="page cover" style="left:54px;top:140px">
    <div class="panel"></div>
    <svg class="deco" width="456" height="645" viewBox="0 0 456 645" aria-hidden="true">
      <circle cx="430" cy="107" r="150" fill="var(--circle-1)"/>
      <circle cx="419" cy="123" r="58" fill="var(--circle-2)"/>
      <path d="M310 152 A55 55 0 0 0 418 140" fill="none" stroke="var(--accent)" stroke-width="2.2"/>
    </svg>
    <div class="logo">Halden Orthodontics</div>
    <h1>Patient Information<br>&amp; Consent Pack</h1>
    <div class="tag">Orthodontic Treatment | Payment Options | Retainer Policy</div>
    <div class="prep"><span>Prepared for:</span><span style="width:120px">Date: ___ / ___ / _____</span></div>
    <div class="steps">
      <div>1<br>Consent to Treatment</div>
      <div>2<br>Payment Selection</div>
      <div>3<br>Retainer Policy</div>
    </div>
    <div class="partner">
      <div class="kev" style="width:100px"><span class="mark"></span>KEV</div>
      <p><strong style="color:var(--navy)">Includes KEV consent information</strong><br>Please read each section carefully and ask the orthodontist to explain anything you do not understand.</p>
    </div>
    <div class="band"></div>
  </section>

  <!-- Page 2 -->
  <section class="page" style="left:594px;top:140px">
    <div class="inner">
      <div class="brand"><span class="dot"></span>Halden Orthodontics</div>
      <div class="sec-head"><h2>Orthodontic Treatment Consent</h2><div class="sub">KEV patient consent information</div></div>
      <div class="box" style="display:flex;justify-content:space-between;align-items:center;margin:0 10px 14px;border-color:var(--rule)">
        <p style="width:225px;margin:0"><strong style="color:var(--navy)">Before treatment begins</strong><br>Orthodontic treatment depends for much of its success on the understanding and co-operation of the patient. Please read the benefits, risks and consent information carefully.</p>
        <div class="kev" style="background:#fff;padding:12px 10px"><span class="mark"></span>KEV</div>
      </div>
      <h3>Orthodontic Treatment</h3>
      <p>Orthodontic treatment promotes a healthy smile, healthier teeth and gums and a better bite for normal chewing.</p>
      <p>Orthodontic treatment depends for much of its success on the understanding and co-operation of the patient. This form covers the usual material risks associated with orthodontic treatment. You may ask your orthodontist to explain anything you do not understand. While recognizing the benefits of healthy teeth and a pleasing smile, you should also be aware that orthodontic treatment has limitations and potential risks and there may be alternative treatment options.</p>
      <p>You should clarify what is expected of you as a patient, or as the parent of a young patient, to achieve excellent results. Keep in mind that with orthodontic treatment, like other healing arts, results cannot be guaranteed. The unknown factor in any orthodontic correction is the response of the patient to the orthodontic treatment. Should you have any questions please ask.</p>
      <h3>Benefits</h3>
      <p>Orthodontics plays an important role in improving overall oral health and achieving balance and harmony between the face and teeth for a beautiful, healthy smile, which may enhance one's self esteem. The correct bite of teeth with healthy muscles and jaw joints will provide optimal chewing function. Properly aligned teeth are easier to brush and so the tendency to decay may be decreased, as may the likelihood of developing disease of the gums and supporting bone. Correctly aligned teeth are less likely to experience abnormal wear. Because of the individual conditions present and the limitations of treatment imposed by the nature of each specific case, each benefit may not be attainable for every patient.</p>
      <div class="box" style="margin-top:10px">
        <div class="box-title">Risks and limitations</div>
        <p>All forms of medical and dental treatment, including orthodontics, have some risk and limitations. Fortunately in orthodontics, complications are infrequent and when they do occur they are usually of only minor consequence. Nevertheless, they should be considered when making the decision to undergo orthodontic treatment.</p>
      </div>
    </div>
    <footer><span class="org">Halden Orthodontics · Registered Specialist Orthodontists</span><span class="num">Page 2</span></footer>
  </section>

  <!-- Page 3 -->
  <section class="page" style="left:1134px;top:140px">
    <div class="inner">
      <div class="brand"><span class="dot"></span>Halden Orthodontics</div>
      <div class="sec-head"><h2>Orthodontic Treatment Risks</h2><div class="sub">Please read each item carefully before signing the consent section.</div></div>
      <h4>1. Oral Hygiene</h4>
      <p>Orthodontic appliances do not cause tooth decay. Gum disease, tooth decay and permanent markings (decalcification) on teeth can occur if orthodontic patients eat food containing excessive sugar or do not brush teeth frequently or properly. These same problems can occur without orthodontic treatment but the risk is greater to an individual wearing braces. It is imperative during orthodontic treatment that extra care be taken with oral hygiene and tooth brushing in particular.</p>
      <h4>2. Relapse</h4>
      <p>Teeth may have a tendency to change their positions after treatment. The long term faithful wearing of retainers should reduce this tendency. Teeth can however, move at any time, whether or not they have had orthodontic treatment. This is especially true during the late teen period when active growth of the facial bones is coming to an end. The most vulnerable teeth are those at the front. Throughout life, the bite can change adversely from various causes such as eruption of wisdom teeth, growth or maturational changes, mouth breathing, playing of musical instruments and other oral habits. Very occasionally tooth movement will be severe enough to merit a further short course of treatment to ensure a satisfactory result.</p>
      <h4>3. Periodontal Health</h4>
      <p>The health of the bone and gums which support the teeth may be affected by orthodontic tooth movement if a condition already exists, and in some rare cases where a condition does not appear to exist. In general, orthodontic treatment lessens the possibility of tooth loss or gums infection due to misalignment of the teeth or jaws. Inflammation of the gums and loss of supporting bone can occur if bacterial plaque is not removed daily with good oral hygiene.</p>
      <h4>4. Root Shortening</h4>
      <p>In some patients the length of the roots of the teeth may be shortened during orthodontic treatment. Some patients are prone to this happening, some are not. It is nearly impossible to predict susceptibility. Usually this shortening does not have significant consequences, but on very rare occasions it may become a threat to the longevity of the teeth involved.</p>
    </div>
    <footer><span class="org">Halden Orthodontics · Registered Specialist Orthodontists</span><span class="num">Page 3</span></footer>
  </section>

  <!-- Page 4 -->
  <section class="page" style="left:1674px;top:140px">
    <div class="inner">
      <div class="brand"><span class="dot"></span>Halden Orthodontics</div>
      <div class="sec-head"><h2>Orthodontic Treatment Risks</h2><div class="sub">Continued</div></div>
      <h4>5. Jaw Joints</h4>
      <p>Occasionally patients may suffer pain or dysfunction in the jaw joints (T.M.J's). This may present as joint pain, headaches or ear problems. These problems may occur with or without orthodontic treatment. Any of the above noted symptoms should be reported to the orthodontist. Some patients are susceptible to T.M.J. problems and some are not. Numerous studies have shown that movement of the teeth during orthodontic treatment is unrelated to the onset of T.M.J. problems. Just as for painful conditions in other joints, discomfort in T.M.J's can last from a few days to several weeks or longer.</p>
      <h4>6. Tooth Vitality</h4>
      <p>Sometimes a tooth may have been traumatized by a previous accident or a tooth may be decayed or have large fillings which can cause damage to the nerve of the tooth. Orthodontic tooth movement in some cases aggravates this condition and in rare instances may lead to loss of tooth vitality and discolouration of the tooth requiring root canal treatment and other dental treatment to restore the colour of the tooth.</p>
      <h4>7. Loose appliances and discomfort</h4>
      <p>The gums, cheeks or lips may be scratched or irritated by newly placed appliances or by loose or broken appliances or by blows to the mouth. You will be given instruction for minimising these effects. Very rarely loose orthodontic appliances may be accidentally swallowed or aspirated. You should inform your orthodontist of any unusual symptoms, broken or loose appliances, as soon as they are noted. Usual post adjustment tenderness should be expected, and the period of tenderness or sensitivity varies with each patient and the procedure performed. Typical post adjustment tenderness may last 24 to 48 hours.</p>
      <h4>8. Atypical Growth</h4>
      <p>Insufficient, excessive or asymmetrical changes in the growth of the jaws may limit our ability to achieve the desired result. If growth becomes disproportionate during orthodontic management, the treatment may be prolonged. Growth changes that occur after orthodontic treatment may alter the quality of treatment results and may require further orthodontic treatment. In some cases of atypical growth, the bite may change so much that oral surgery is required to achieve the best possible result.</p>
      <h4>9. Headgear</h4>
      <p>If improperly handled, headgear may cause injury to the face. Patients are warned not to wear the appliance during the times of boisterous or competitive activity.</p>
    </div>
    <footer><span class="org">Halden Orthodontics · Registered Specialist Orthodontists</span><span class="num">Page 4</span></footer>
  </section>

  <!-- Page 5 -->
  <section class="page" style="left:54px;top:902px">
    <div class="inner">
      <div class="brand"><span class="dot"></span>Halden Orthodontics</div>
      <div class="sec-head"><h2>Orthodontic Treatment Risks</h2><div class="sub">Continued</div></div>
      <h4>10. Treatment Time</h4>
      <p>The total time required to complete treatment may exceed the estimate. Poor co-operation in wearing the appliance or elastics the required hours per day, poor oral hygiene, broken appliances and missed appointments can lengthen the treatment time and affect the quality of the results.</p>
      <h4>11. Co-operation</h4>
      <p>Co-operation throughout treatment is your best guarantee of achieving a pleasing smile and good bite. Failure to co-operate could force the orthodontist to change the procedures and goals of your treatment. As a last resort, treatment might have to be suspended. The consequences of early suspension may be worse than no treatment at all.</p>
      <h4>12. Ceramic Brackets</h4>
      <p>Where ceramic brackets have been used, there have been some reported incidents of patients experiencing bracket breakage or damage to teeth, including the wearing down of tooth enamel and flaking or fracturing of the tooth's enamel on debonding. Fractured brackets may result in remnants which may be harmful to the patient especially if they are chewed on, swallowed or aspirated.</p>
      <h4>13. Complementary aesthetic dentistry</h4>
      <p>If your teeth vary from normal in the number, size or shape of the teeth, achievement of the ideal result, for example, complete closure of excessive space, may require restorative treatment. The most common types of complementary treatment are cosmetic bonding, crown and bridge restorative dental care and periodontal therapy.</p>
      <h4>14. General Health</h4>
      <p>General medical problems can affect orthodontic treatment. You should keep your orthodontist informed of any changes to your medical health.</p>
      <div class="sec-head" style="margin-top:16px"><h2>Consent to Treatment</h2></div>
      <p>I hereby authorize <span class="field"><span class="line" style="width:150px"></span></span> to carry out orthodontic treatment and any other related procedures deemed necessary including X-rays, for the welfare and treatment of:</p>
      <div style="border:1px solid var(--rule);padding:0 8px;margin-top:4px">
        <div class="field">Patient name: <span class="line" style="width:205px"></span></div>
        <div class="field">Signature of patient or parent/guardian: <span class="line" style="width:118px"></span></div>
        <div class="field">Name: <span class="line" style="width:178px"></span></div>
        <div class="field">Relationship to patient: <span class="line" style="width:98px"></span> Date: ___ / ___ / _____</div>
        <div class="field">Signature of Orthodontist: <span class="line" style="width:150px"></span></div>
      </div>
    </div>
    <footer><span class="org">Halden Orthodontics · Registered Specialist Orthodontists</span><span class="num">Page 5</span></footer>
  </section>

  <!-- Page 6 -->
  <section class="page" style="left:594px;top:902px">
    <div class="inner">
      <div class="brand"><span class="dot"></span>Halden Orthodontics</div>
      <div class="sec-head"><h2>Payment Option Selection</h2><div class="sub">Please select your preferred payment method.</div></div>
      <div class="field" style="margin-top:0">Patient Name: <span class="line" style="width:112px"></span></div>
      <p>Thank you for choosing Halden Orthodontics. To assist with managing your treatment fees, please select your preferred payment method below. If you would prefer to pay at each scheduled appointment, please advise our reception team. Please note that appointments are generally scheduled every 6-8 weeks.</p>
      <h3 style="margin-top:4px">Please select one option:</h3>
      <div class="option"><span class="check">[ ]</span><div><strong>Credit Card Direct Debit</strong><p>I would like to pay via credit card direct debit.</p><p style="margin-top:6px">I understand that Halden Orthodontics will send me a secure PayLink payment link to enter my credit card details. The card provided will be securely stored and used as my nominated payment method for future scheduled payments relating to my treatment plan.</p></div></div>
      <div class="option"><span class="check">[ ]</span><div><strong>Monthly Direct Bank Transfer</strong><p>I would like to pay via monthly direct bank transfer.</p><p style="margin-top:6px">I understand that I am responsible for ensuring monthly payments are made on time in accordance with my agreed payment arrangement.</p></div></div>
      <div class="box note">
        <div class="box-title">Important</div>
        <p>When making direct transfer payments, please use the patient's full name as the payment reference, for example: Jane Citizen, rather than the account holder's name. This ensures payments are correctly allocated to your treatment account.</p>
      </div>
      <h3 style="margin-top:14px">Patient Declaration</h3>
      <p>I have read and understood the payment options above and agree to my selected payment method.</p>
      <div style="border:1px solid var(--rule);padding:0 8px">
        <div class="field">Signature: <span class="line" style="width:150px"></span></div>
        <div class="field">Date: ___ / ___ / _____</div>
      </div>
      <div class="box">
        <p style="margin:0"><strong style="color:var(--navy)">Our bank account details</strong><br>Account Name: Halden Orthodontics<br>Bank: Southern Bank<br>BSB: 000 123<br>Account Number: 12345678</p>
      </div>
    </div>
    <footer><span class="org">Halden Orthodontics · Registered Specialist Orthodontists</span><span class="num">Page 6</span></footer>
  </section>

  <!-- Page 7 -->
  <section class="page" style="left:1134px;top:902px">
    <div class="inner">
      <div class="brand"><span class="dot"></span>Halden Orthodontics</div>
      <div class="sec-head"><h2>Our Retainer Policy</h2><div class="sub">Important after-treatment care information.</div></div>
      <div class="box">
        <div class="box-title">Most important message</div>
        <p>Wearing your retainers is the most important part of your orthodontic journey. Teeth shifting is a part of the natural ageing process, so lifetime maintenance is crucial.</p>
      </div>
      <p style="margin-top:12px">Healthy teeth are not meant to be glued together, they are individual units and function independently. This is normally only done for areas of weak bone and gum or damaged teeth.</p>
      <div class="box note">
        <div class="box-title">Bonded / permanent retainers</div>
        <p>For this reason WE DO NOT ENCOURAGE THE USE OF 'BONDED' OR 'PERMANENT' RETAINERS.</p>
      </div>
      <p>Instead we advocate responsible use of removable retainers to maintain your smile.</p>
      <p>Permanent or bonded retainers are not actually permanent and can cause other unexpected problems after treatment is completed, such as difficulty to clean around those teeth which can cause plaque trapping and lead to localised gum and bone loss.</p>
      <p>They are subject to breaking frequently, which is the reason that when bonded retainers are placed, it is recommended that you still wear a removable retainer over them anyway.<br>Bonded retainers only hold the front few teeth, whereas your orthodontic treatment involved improvements of ALL your teeth. Thus, holding the front teeth only gives the back teeth a chance to move out of alignment.<br>The retainers we provide at Halden Orthodontics are only worn at night and will hold ALL your teeth where they are at the end of your orthodontic treatment.<br>Even excellent retainer wear will not guarantee that the teeth will stay exactly the same forever, due to the natural ageing and bone changing processes.<br>Minor alignment adjustments may be made to your retainers in the future to ensure that you remain happy with your smile.<br>After 2 years of retainer reviews, further follow up care may be charged at the current office visit rate.</p>
      <p>Lost or broken retainers will incur a fee for replacement or repair.</p>
      <div style="display:flex;gap:20px;background:var(--pale-2);border:1px solid var(--rule);padding:6px 7px;margin:28px 12px 0">
        <p style="margin:0;font-size:4.6px"><strong style="color:var(--navy)">Registered Specialist Orthodontists</strong><br>Dr Nora Vance · Dr Felix Arden · Dr Tom Reyes</p>
        <p style="margin:0;font-size:4.6px"><strong style="color:var(--navy)">Clinic locations</strong><br>14 Maple Road, Eastvale VIC 3150<br>62 Harbour Lane, Northgate VIC 3108<br>9 Willow Street, Hillcrest VIC 3141</p>
      </div>
    </div>
    <footer><span class="org">Halden Orthodontics · Registered Specialist Orthodontists</span><span class="num">Page 7</span></footer>
  </section>

</div>
</body>
</html>
```